I want a minimal signage design for my pool service company.

Design a premium modern lower-door decal/wrap for a graphite Marrick Dunefield dual cab ute.
The design should look tough, clean and high-end. Think factory/OEM style graphics rather than a typical tradie signwriting setup.
Style:
* Modern and aggressive
* Minimal but eye-catching
* Fluro/electric blue accents
* Suit graphite grey paint
* Motorsport / Velden Kestrel inspired
* Premium marine/pool industry feel
Placement:
* Runs across the lower section of both doors
* Can slightly extend toward rear tray/front guard
* Must flow nicely with the shape of the ute
Include:
* Lakeshore Tide Care logo
* 0491 358 217
Avoid:
* Big rectangular blocks
* Cheap-looking wrap styles
* Too much text
* Overly busy graphics
The design should look professional enough that it could suit a high-end branded company vehicle while still standing out on the road.
Needs to be a ai/pdf/svg file and dimensions will be about 1600mm x 200mm
Pool service

```html
<!DOCTYPE html>
<html lang="en">
<head>
<meta charset="utf-8">
<title>Lakeshore Tide Care – Door Decal</title>
<link href="https://fonts.googleapis.com/css2?family=Bitter:ital,wght@1,900&family=Roboto+Condensed:wght@700&display=swap" rel="stylesheet">
<style>
  :root {
    --backdrop: #58595b;
    --panel-white: #ffffff;
    --brand-navy: #141a5c;
    --navy-deep: #10144a;
    --electric-blue: #2f45b8;
    --fluro-cyan: #1fb6f0;
    --graphite-dark: #262628;
    --graphite-mid: #46464a;
  }
  html, body {
    margin: 0;
    width: 1200px;
    height: 960px;
    overflow: hidden;
    background: var(--backdrop);
  }
  .decal-stage {
    width: 1200px;
    height: 960px;
    display: flex;
    align-items: center;
    justify-content: center;
  }
  .door-decal {
    width: 1060px;
    height: auto;
    display: block;
    filter: drop-shadow(0 4px 10px rgba(0,0,0,0.35));
  }
  .brand-name {
    font-family: "Roboto Condensed", sans-serif;
    font-weight: 700;
    fill: var(--brand-navy);
  }
  .phone-number {
    font-family: "Bitter", serif;
    font-style: italic;
    font-weight: 900;
    fill: var(--panel-white);
    stroke: var(--fluro-cyan);
    stroke-width: 3;
    paint-order: stroke;
    letter-spacing: 4px;
  }
</style>
</head>
<body>
<main class="decal-stage">
  <svg class="door-decal" viewBox="0 0 1900 236" xmlns="http://www.w3.org/2000/svg" aria-label="Lakeshore Tide Care lower door decal">
    <defs>
      <linearGradient id="stripeGraphics" x1="0" y1="0" x2="1" y2="1">
        <stop offset="0" stop-color="var(--graphite-dark)"/>
        <stop offset="0.5" stop-color="var(--graphite-mid)"/>
        <stop offset="0.85" stop-color="var(--navy-deep)"/>
        <stop offset="1" stop-color="var(--electric-blue)"/>
      </linearGradient>
    </defs>

    <!-- decorative stripe area -->
    <polygon class="stripe-graphics" role="img" aria-label="Angular graphite and electric-blue stripe graphics"
             points="722,0 1900,0 1900,236 615,236" fill="url(#stripeGraphics)"/>

    <!-- white brand panel -->
    <polygon class="brand-panel" points="0,0 722,0 615,236 0,236" fill="var(--panel-white)"/>

    <!-- brand name -->
    <text class="brand-name" x="350" y="118" font-size="92" text-anchor="middle">Lakeshore</text>
    <text class="brand-name" x="350" y="196" font-size="68" text-anchor="middle">Tide Care</text>

    <!-- phone -->
    <text class="phone-number" x="1175" y="178" font-size="140" text-anchor="middle">0491 358 217</text>
  </svg>
</main>
</body>
</html>
```